Education / Investment Website Design (PDF Wireframe Provided)

More details are in the wireframe document

We need a website design for an investment education company. Our Clients purchase education courses through us. We use meridian toolkit (Wordpress) for our website. We just require the graphics in PSD (not coded) for the

1. Homepage - brightfunnelhub.com style
2. Blog page - brightfunnelhub.com style
3. Single Blog Post
4. Product page - Lernova.com style
5. Single Product Page - https://www.lernova.com/share-market-class-oceania/?ref=kP7qLmW3xT9Z
6. Contact Us Page (Contact Us Form, Map and Contact details)
7. About Us Page

See the attached Wireframe for the homepage

IMPORTANT
Websites we like are clean, white, similar to BrightFunnelHub.com and Lernova.com
Use of white space, big fonts, flat buttons

Attached wireframe is the flow of the homepage. (Homepage brief PDF)

Each section represents a "fold" as visitors are scrolling down. (Homepage showing folds PDF - how the visitor sees each section of the homepage as they scroll down the homepage)

We've got a clear idea of the elements on the page and looking for a great graphic / web designer to create those for us. (We do the coding)

Website currently is: southerncrosswealthschool.com.au (we want to simplify the website and have a more modern / flat design)

Questions: Please ask

Target Market(s)

Investors, People looking for Investment / Financial Education

Industry/Entity Type

Investment

Number of Pages Required

5+ page

Font styles to use
Sans Serif

Requirements
Must have
• Similar Items listed in the wireframe
• Clean Look - Flat design - elegant
• Roll-over (mouse on / mouse off) for Buttons and Top Banner Selection
Should not have
• Images that looks too much like "Stock Images"
• Please avoid bright orange

```html
<!DOCTYPE html>
<html lang="en">
<head>
<meta charset="utf-8">
<title>Is The Economy Stumbling, Or Is This Business As Usual? | Southern Cross Wealth School</title>
<link rel="stylesheet" href="https://fonts.googleapis.com/css2?family=Open+Sans:wght@400;600;700;800&display=swap">
<style>
:root{
  --teal:#45bcae;
  --teal-dark:#2fa595;
  --teal-soft:#5cc8b8;
  --green:#6cc49a;
  --ink:#2c2c2c;
  --text:#555;
  --muted:#999;
  --line:#e4e4e4;
  --panel:#f4f4f4;
  --footer:#2a2d2f;
  --footer-deep:#1f2123;
  --blue:#3b5a98;
  --sky:#3aa6dd;
  --red:#d54a3b;
}
*{box-sizing:border-box;margin:0;padding:0}
html,body{width:1200px;height:5122px;overflow:hidden}
body{font-family:"Open Sans",Arial,sans-serif;color:var(--text);background:#fff;font-size:13px;line-height:1.75}
.page{position:relative;width:1200px;height:5122px;overflow:hidden}
a{color:var(--teal);text-decoration:none}
.wrap{width:960px;margin:0 auto;position:relative}

/* top notice */
.notice-bar{background:var(--teal);color:#fff;font-size:12px;height:30px;line-height:30px}
.notice-bar .wrap{padding-left:0}

/* header */
.site-header{height:84px;border-bottom:1px solid var(--line)}
.site-header .wrap{display:flex;align-items:center;height:84px}
.brand{display:flex;align-items:center;gap:10px;width:290px}
.brand-mark{width:34px;height:34px;background:var(--teal);border-radius:3px}
.brand-name{font-weight:700;font-size:15px;color:var(--ink);line-height:1.15}
.main-nav{display:flex;gap:26px;margin-left:40px}
.main-nav a{font-size:11px;font-weight:700;color:var(--muted);letter-spacing:.5px}
.main-nav a.active{color:var(--teal)}
.social-dots{display:flex;gap:6px;margin-left:28px}
.social-dots span{width:22px;height:22px;border-radius:50%;background:#bbb}
.account-links{margin-left:auto;text-align:right;font-size:11px;line-height:1.5}
.account-links a{display:block;color:var(--muted)}

/* layout */
.content{display:flex;gap:30px;padding-top:26px}
.post{width:650px}
.sidebar{width:280px}

.post-title{font-size:38px;line-height:1.2;font-weight:800;color:var(--ink);letter-spacing:-.5px}
.post-meta{font-size:11px;color:var(--muted);margin:10px 0 14px}
.hero{height:360px;background:linear-gradient(135deg,#d9d9d9,#9a9a9a 55%,#cfcfcf)}
.share-row{display:flex;gap:6px;margin:16px 0 12px}
.share{height:24px;min-width:64px;border-radius:2px;color:#fff;font-size:11px;font-weight:700;display:flex;align-items:center;justify-content:flex-end;padding:0 8px}
.share::before{content:"";width:10px;height:10px;background:rgba(255,255,255,.7);border-radius:2px;margin-right:auto}
.s1{background:var(--blue)}.s2{background:var(--sky)}.s3{background:var(--red)}.s4{background:#0077b5}.s5{background:#888}.s6{background:var(--teal)}
.categories{font-size:11px;color:var(--muted);margin-bottom:22px}
.article p{margin-bottom:14px}
.article h2{font-size:17px;font-weight:700;color:var(--ink);margin:24px 0 10px}
.article ul{margin:0 0 14px 18px}
.article li{margin-bottom:10px}

/* author */
.author-box{background:var(--teal);color:#fff;padding:30px;display:flex;gap:24px;margin-top:36px;height:250px}
.author-photo{width:96px;height:96px;border-radius:50%;background:linear-gradient(135deg,#e8e2da,#9c8f84);flex:none}
.author-box h3{font-size:20px;font-weight:700;margin-bottom:8px}
.author-box p{font-size:12px;line-height:1.7}
.author-box a{color:#fff;font-weight:700;display:block;margin-top:10px;font-size:12px}

/* related */
.related{border:1px solid var(--line);margin-top:40px;padding:26px 30px;height:520px}
.related h3{font-size:20px;font-weight:700;color:var(--ink);margin-bottom:20px;display:flex;align-items:center;gap:10px}
.related h3::before{content:"";width:22px;height:22px;border-radius:50%;background:var(--teal)}
.related-grid{display:grid;grid-template-columns:repeat(3,1fr);gap:20px}
.related-item .thumb{height:110px;margin-bottom:8px}
.related-item p{font-size:12px;color:var(--ink);line-height:1.5}
.t1{background:linear-gradient(135deg,#c9c0b5,#8a7d70)}
.t2{background:linear-gradient(135deg,#e0d9cf,#b4a694)}
.t3{background:linear-gradient(135deg,#7fb0d6,#4d7fa8)}
.t4{background:linear-gradient(135deg,#c4d6e3,#6e8ea8)}
.t5{background:linear-gradient(135deg,#d8cfc5,#7a6d62)}
.prev-link{display:block;margin:20px 0 0;font-size:12px;font-weight:600}

/* discussion */
.discussion h3{font-size:20px;font-weight:700;color:var(--teal);margin:40px 0 14px}
.comment{background:var(--panel);padding:20px;display:flex;gap:16px;height:170px;position:relative}
.comment .avatar{width:44px;height:44px;border-radius:50%;background:#c9c9c9;flex:none}
.comment strong{color:var(--ink);font-size:13px}
.comment small{display:block;color:var(--muted);font-size:10px;margin-bottom:6px}
.comment p{font-size:12px;line-height:1.6}
.btn{background:var(--teal);color:#fff;font-weight:700;font-size:12px;border:0;padding:9px 28px;border-radius:2px;letter-spacing:.5px}
.comment .btn{position:absolute;right:20px;bottom:18px}

.reply h3{font-size:34px;font-weight:800;color:var(--ink);margin:50px 0 6px}
.reply .note{font-size:12px;color:var(--muted);margin-bottom:18px}
.field{border:1px solid var(--line);height:38px;width:300px;margin-bottom:12px;font-size:11px;color:#aaa;padding:10px 12px}
.field.area{width:650px;height:140px}
.reply .btn{display:block;margin:10px 0 0 auto}

/* sidebar */
.cta{display:flex;align-items:center;gap:12px;color:#fff;font-weight:700;font-size:12px;height:48px;padding:0 14px;margin-bottom:4px}
.cta svg{flex:none}
.c1{background:var(--teal-dark)}.c2{background:var(--teal)}.c3{background:var(--green)}
.popular{background:var(--panel);margin-top:22px;padding:20px;height:990px}
.popular h3{font-size:18px;font-weight:700;color:var(--ink);margin-bottom:12px}
.popular a{display:block;font-size:12px;line-height:1.5;padding:9px 0;border-bottom:1px solid #e2e2e2;color:var(--teal)}

/* footer */
.site-footer{position:absolute;left:0;right:0;bottom:0;height:568px;background:var(--footer);color:#aaa;font-size:11px}
.footer-cols{display:flex;padding-top:40px;gap:40px;height:250px}
.footer-brand{width:300px}
.footer-brand .brand-name{color:#fff;margin-bottom:12px;display:flex;align-items:center;gap:10px}
.footer-brand .brand-mark{width:26px;height:26px}
.footer-col h4{color:#fff;font-size:13px;font-weight:700;margin-bottom:10px}
.footer-col a{display:block;color:#aaa;line-height:1.9}
.footer-col{width:130px}
.footer-col.connect{width:180px}
.footer-col.connect .dots{display:flex;gap:8px}
.footer-col.connect .dots span{width:28px;height:28px;border-radius:50%;background:#555}
.customer-notice{border-top:1px solid #3a3d40;padding-top:24px}
.customer-notice h4{color:#fff;font-size:12px;font-weight:700;margin-bottom:8px}
.customer-notice p{line-height:1.7;margin-bottom:10px}
.footer-bottom{position:absolute;left:0;right:0;bottom:0;height:44px;background:var(--footer-deep);line-height:44px}
.footer-bottom .wrap{display:flex;justify-content:space-between}
.footer-bottom a{color:#aaa;margin-left:14px}
</style>
</head>
<body>
<div class="page">

<div class="notice-bar"><div class="wrap">First time visitor? Then start here! Learn more about Southern Cross Wealth School</div></div>

<header class="site-header">
  <div class="wrap">
    <div class="brand"><span class="brand-mark"></span><span class="brand-name">Southern Cross<br>Wealth School</span></div>
    <nav class="main-nav"><a href="#">HOME</a><a href="#" class="active">BLOG</a><a href="#">ABOUT US</a><a href="#">MEMBERS</a></nav>
    <div class="social-dots"><span></span><span></span><span></span><span></span></div>
    <div class="account-links"><a href="#">Sign in</a><a href="#">Join</a><a href="#">Log out</a></div>
  </div>
</header>

<div class="wrap content">
  <main class="post">
    <h1 class="post-title">Is The Economy Stumbling, Or Is This Business As Usual?</h1>
    <div class="post-meta">June 18th, 2015 by Daniel Hartley &nbsp;|&nbsp; 22 Readers</div>
    <div class="hero" role="img" aria-label="Photo of stacked financial newspapers with market headlines"></div>

    <div class="share-row"><span class="share s1">212</span><span class="share s2">34</span><span class="share s3">12</span><span class="share s4">8</span><span class="share s5">5</span><span class="share s6">261</span></div>
    <div class="categories">Categories: <a href="#">Blog</a>, <a href="#">Is The Economy Stumbling, Or Is This Business As Usual?</a></div>

    <div class="article">
      <p>The US economy has failed to improve over recent months, and at the same time the local economy is showing signs of weakness in key sectors. This begs the question of whether or not a recession is just around the corner. Investors certainly are starting to panic.</p>
      <p>The Federal Reserve chair Helen Marsh released the Federal Open Market Committee statement on Wednesday, downgrading forecasts for the US economy over the coming year. While the committee hinted towards a point in time when it would raise interest rates, little has caused the US dollar to rise substantially. But the world's benchmark currency has started falling as it becomes more apparent that an interest rate rise is not likely any time soon.</p>

      <h2>Globally, the economic picture is not very rosy.</h2>
      <ul>
        <li>Despite the problems stemming from Greece, the Eurozone remains in a weak state with latest figures showing a 0.4% annual GDP growth rate. This had been negative up until late 2013. Looking at any one of the major economies, inflation has been negative for the last few months, reflecting a contracting economy.</li>
        <li>With the strongest annual GDP growth rate of any nation in the world, China is still considered to be in trouble. Over the last year, we have seen a decrease from 7.5% to 7.0%. The impact to major trade partners is clearly evident.</li>
        <li>Japan has been fluctuating between recession and weak growth for years. In the latest quarterly report, the economy has bowed to its way back to growth at 0.1% annual GDP growth rate. At the same time, inflation at 0.6% having declined from 3.7% in May 2014 means the fiscal rate of growth remains negative.</li>
        <li>The US has fluctuated improvement in their annual GDP growth rate over the last 2 years, improving from a low of 1.8% to 2.9%. Roaring in its bounce is inflation reaching a goal of 2% and a slow decline in the unemployment rate, which is currently at 5.5%. However, without some inflation, the economy is not growing.</li>
        <li>Closer to home, the local economy has shown very little growth in the last few years. Recent data shows an annual GDP growth rate of 2.3%. Inflation has more than halved in the last 18 months to 1.3%, but unemployment remains high at 6.1%.</li>
      </ul>
      <p>Our major trade partners are suffering from stagnating economies with very little growth prospects. Although China continues to grow, our Mining sector is already feeling the pinch. Add to this the sharp decline in commodity prices and our leading Mining companies are not making the same profit margins as during the boom of the last few years.</p>
      <p>Banks are quite highly valued at the moment, and some would consider they are inflated above their fair value. This has helped trigger a sell-off this week on the exchange, which has dropped nearly 200 points (or 3.4%) in 4 days.</p>

      <h2>Analysts are now discussing what opportunities lie ahead</h2>
      <p>Following the GFC of 2008-09, the US economy had experienced growth on the back of years of Quantitative Easing (QE), or stimulus measures. With that program ending last year the economy has failed to improve substantially. In essence, it is failing to improve on its own two feet. And without any additional reason for economic improvement, may require further stimulus to start growing again.</p>
      <p>Europe and Japan have recently adopted QE programs in an effort to boost their economies. This should reflect how desperate they are for growth. Through the US QE programs, it has been proven that this does help the economy, but must be continued until such time that the economy can independently grow on its own. And how long will that take?</p>
      <p>The local market, on the other hand, has been heavily reliant on the growth of China in recent years. Now that this boom has come to an end, the government is undergoing campaigns to create new industry income through fields such as Medical knowledge and technology.</p>

      <h2>Where to from here?</h2>
      <p>The Southern Reserve Board is scheduled to release their interest rate statement on Tuesday 4th May. The probability of an interest rate cut has improved, especially on the back of weaker economic data. This would help stimulate the economy slightly, but will it be enough to create confidence amongst investors?</p>
      <p>Not likely. Investors are lacking direct for some hefty headwinds. Our major trade partners are China, US and Japan. None of those economies are performing particularly well. And without that to help boost our trade exports, we are not likely to be able to create new prosperity internally.</p>
      <p>There are some hard roads ahead for investors. The Southern Share Exchange (SSX), as represented by the SSX200 index, has hit 8 data points a times since late February. This has formed a trading range or consolidation period.</p>

      <h2>SSX200 highs and lows...</h2>
      <p>For the first half of the week, we have seen the SSX200 release from those highs to the medium term lows, quickly, and without any hesitation. This has some investors worried. But an interest Rate drop next Tuesday will help boost investor confidence slightly. Which might help stem a decline in the market.</p>
      <p>However, if we find rates are kept on hold next Tuesday, this could send the stock market lower. As long as investors don't 'panic sell', we could ride through any mild market declines.</p>
      <p>On a positive note, there was confidence earlier in the year, driving the SSX200 up more than 15% in February-March. If we have a market retracement in coming weeks, this could be viewed as a more effective accumulation level for stocks, which have probably been overbought. That could lead to a more promising finish to the year.</p>
      <p>In essence, investor confidence is stumbling a little, but it is not panic stations just yet. Slow growth is expected on the short term, but in the meantime, it is business as usual.</p>
      <p>To learn more about these strategies <a href="#">Click Here</a></p>
    </div>

    <div class="share-row"><span class="share s1">212</span><span class="share s2">34</span><span class="share s3">12</span><span class="share s4">8</span><span class="share s5">5</span><span class="share s6">261</span></div>

    <section class="author-box">
      <div class="author-photo" role="img" aria-label="Portrait photo of the author"></div>
      <div>
        <h3>About Daniel Hartley</h3>
        <p>Daniel Hartley has been involved in the financial services industry since 2009 as a share trader, coach and mentor. He has a keen interest in technical analysis, trading plans, funds management and education services. His passion is using stocks and index options to enhance investment strategies. No matter whether the markets are rising or falling, the opportunities to profit in the markets are limitless!</p>
        <a href="#">View all posts by Daniel Hartley &rarr;</a>
      </div>
    </section>

    <section class="related">
      <h3>Related Posts</h3>
      <div class="related-grid">
        <div class="related-item"><div class="thumb t1" role="img" aria-label="Photo of a fast food restaurant sign"></div><p>What you can learn from a fast food giant and apply to today's high tech market leader?</p></div>
        <div class="related-item"><div class="thumb t2" role="img" aria-label="Photo of a desk with charts"></div><p>Looking at the future up close and now</p></div>
        <div class="related-item"><div class="thumb t3" role="img" aria-label="Photo of a flag over a city"></div><p>Cuba – the new 'Emerging Market' kid on the block</p></div>
        <div class="related-item"><div class="thumb t4" role="img" aria-label="Photo of a sailboat on open water"></div><p>Stop being scared of your own shadow and start making money</p></div>
        <div class="related-item"><div class="thumb t5" role="img" aria-label="Photo of gold bars"></div><p>Watch out if you have chased gold in the property or the stock market</p></div>
      </div>
    </section>
    <a class="prev-link" href="#">&larr; Previous Post</a>

    <section class="discussion">
      <h3>Discussion</h3>
      <div class="comment">
        <div class="avatar"></div>
        <div>
          <strong>John Doe</strong><small>May 8, 2015 at 10:20 am</small>
          <p>Hey Daniel,<br>Very interesting. I must say I'm new to the investing game and think it's a great way you broke it down for me. I look forward to finding more outcomes and ways that need to be compared in order to touch your target.<br>Thanks for sharing.</p>
        </div>
        <button class="btn">REPLY</button>
      </div>
    </section>

    <section class="reply">
      <h3>Leave a Reply</h3>
      <p class="note">Your email address will not be published. Required fields are marked *</p>
      <div class="field">Name *</div>
      <div class="field">Email *</div>
      <div class="field">Website</div>
      <div class="field area">Comment</div>
      <button class="btn">POST COMMENT</button>
    </section>
  </main>

  <aside class="sidebar">
    <a class="cta c1" href="#"><svg width="22" height="22" viewBox="0 0 22 22"><rect x="2" y="4" width="18" height="14" fill="none" stroke="#fff" stroke-width="2"/></svg>TEACH ME HOW TO TRADE</a>
    <a class="cta c2" href="#"><svg width="22" height="22" viewBox="0 0 22 22"><polyline points="2,16 8,10 12,13 20,5" fill="none" stroke="#fff" stroke-width="2"/></svg>TELL ME WHAT SHOULD I TRADE</a>
    <a class="cta c3" href="#"><svg width="22" height="22" viewBox="0 0 22 22"><polyline points="4,11 9,16 18,6" fill="none" stroke="#fff" stroke-width="2.5"/></svg>DO IT ALL THE WORK FOR ME</a>

    <section class="popular">
      <h3>Popular Posts</h3>
      <a href="#">Looking At The Future Up Close And Now</a>
      <a href="#">What you can learn from a fast food giant and apply to today's high tech market leader?</a>
      <a href="#">Gold Price Forecast 2014 – All that glitters is not gold!</a>
      <a href="#">Cuba – the new 'Emerging Market' kid on the block</a>
      <a href="#">Stop being scared of your own shadow and start making money</a>
      <a href="#">Watch out if you have chased gold in the property or the stock market, here or in the US – then make sure you don't get caught on the wrong side of this crunch as it will hurt.</a>
      <a href="#">Gold Price Forecast 2014 – All that glitters is not gold!</a>
      <a href="#">Cuba – the new 'Emerging Market' kid on the block</a>
      <a href="#">Stop being scared of your own shadow and start making money</a>
      <a href="#">Looking At The Future Up Close And Now</a>
      <a href="#">What you can learn from a fast food giant and apply to today's high tech market leader?</a>
      <a href="#">Watch out if you have chased gold in the property or the stock market, here or in the US – then make sure you don't get caught on the wrong side of this crunch as it will hurt.</a>
      <a href="#">Gold Price Forecast 2014 – All that glitters is not gold!</a>
    </section>
  </aside>
</div>

<footer class="site-footer">
  <div class="wrap">
    <div class="footer-cols">
      <div class="footer-brand">
        <div class="brand-name"><span class="brand-mark"></span>Southern Cross Wealth School</div>
        <p>TradeNest is a registered trademark of Southern Cross Wealth School Pty Ltd. All courses are delivered online and in person across the region.</p>
      </div>
      <div class="footer-col"><h4>Main Menu</h4><a href="#">Home</a><a href="#">Courses</a><a href="#">Blog</a><a href="#">About Us</a><a href="#">Contact</a></div>
      <div class="footer-col"><h4>Courses</h4><a href="#">Discovery</a><a href="#">Foundation</a><a href="#">Options</a><a href="#">Mentoring</a><a href="#">Webinar</a></div>
      <div class="footer-col"><h4>Other</h4><a href="#">Members</a><a href="#">Privacy</a><a href="#">Terms</a><a href="#">Sitemap</a></div>
      <div class="footer-col connect"><h4>Connect with us</h4><div class="dots"><span></span><span></span><span></span><span></span></div></div>
    </div>
    <div class="customer-notice">
      <h4>CUSTOMER NOTICE</h4>
      <p>SOUTHERN CROSS WEALTH SCHOOL PTY LTD provides general education only. It does not take into account your objectives, financial situation or needs, and you should consider whether any information is appropriate for you before acting on it. Past performance is not a reliable indicator of future performance. Trading in shares, options and other derivatives involves risk and you may lose more than your initial investment. Any examples used in our courses and articles are for educational purposes only and are not a recommendation to buy or sell any financial product. You should obtain independent advice from a licensed adviser before making any investment decision.</p>
      <p>Southern Cross Wealth School Pty Ltd, Level 4, 120 Harbour Street, Port Lindell NSW 2000. Phone 1300 555 014.</p>
    </div>
  </div>
  <div class="footer-bottom"><div class="wrap"><span>&copy; Copyright 2015 SCWS – All Rights Reserved</span><span><a href="#">Terms And Conditions</a><a href="#">Privacy Policy</a></span></div></div>
</footer>

</div>
</body>
</html>
```